Business Card Design

Harbor Refuse 342 is a waste collection business contracted to remove waste from city streets, parks and caravan parks.

Target Market(s)

CEO and Managing Directors

Industry/Entity Type

Business

Contact Information for Business Card

Harbor Refuse 342
Manager
Dale Pickett
0439516204
harborrefuse342@quillmail.com.au

Colors
33a6d7
ecf7fb

Requirements
Must have
• Must have eye catching design that stands out above others ( tender process can be very competitive ).
Nice to have
• A garbage truck on or in the logo somehow

```html
<!DOCTYPE html>
<html lang="en">
<head>
<meta charset="utf-8">
<title>Harbor Refuse 342 — Business Card</title>
<link href="https://fonts.googleapis.com/css2?family=Montserrat:wght@500;600;700&display=swap" rel="stylesheet">
<style>
  :root {
    --card-white: #ffffff;
    --card-tint: #ecf7fb;
    --ink: #161616;
    --ink-soft: #2a2a2a;
    --brand-yellow: #f8d00f;
    --brand-blue: #33a6d7;
    --truck-green: #3fae3a;
    --truck-deep: #2f8f35;
    --truck-grey: #8a8f94;
    --on-blue: #ffffff;
  }
  * { margin: 0; padding: 0; box-sizing: border-box; }
  html, body {
    width: 1200px;
    height: 720px;
    overflow: hidden;
    background: var(--card-white);
  }
  .card {
    position: relative;
    width: 1200px;
    height: 720px;
    overflow: hidden;
    background: linear-gradient(180deg, var(--card-white) 0%, var(--card-white) 40%, var(--card-tint) 100%);
    font-family: "Montserrat", Arial, sans-serif;
    color: var(--ink);
  }
  .bands {
    position: absolute;
    left: 0;
    top: 0;
    width: 1200px;
    height: 720px;
  }
  .band-yellow { fill: var(--brand-yellow); }
  .band-blue { fill: var(--brand-blue); }

  .holder {
    position: absolute;
    right: 76px;
    top: 100px;
    text-align: right;
  }
  .holder-name {
    font-size: 40px;
    font-weight: 700;
    line-height: 1.15;
    color: var(--ink);
  }
  .holder-role {
    font-size: 28px;
    font-weight: 600;
    line-height: 1.2;
    color: var(--ink-soft);
  }

  .truck-art {
    position: absolute;
    left: 267px;
    top: 236px;
    width: 288px;
    height: 227px;
    border-radius: 18px;
    background: radial-gradient(ellipse at 45% 45%, var(--truck-green) 0%, var(--truck-deep) 55%, var(--truck-grey) 100%);
  }

  .brand-name {
    position: absolute;
    left: 560px;
    top: 232px;
    width: 400px;
    font-weight: 700;
    color: var(--ink);
    line-height: 1;
  }
  .brand-name .word-line {
    display: block;
    font-size: 50px;
    white-space: nowrap;
  }
  .brand-name .number-line {
    display: block;
    font-size: 118px;
    margin-top: 8px;
    padding-left: 95px;
  }

  .contact-email {
    position: absolute;
    left: 76px;
    top: 586px;
    display: flex;
    align-items: center;
    height: 40px;
    font-size: 23px;
    font-weight: 600;
    color: var(--ink);
    white-space: nowrap;
  }
  .contact-icon {
    width: 32px;
    height: 32px;
    margin-right: 14px;
    flex: none;
  }

  .phone {
    position: absolute;
    left: 825px;
    top: 583px;
    display: flex;
    align-items: center;
    height: 46px;
    font-size: 38px;
    font-weight: 700;
    color: var(--on-blue);
  }
  .phone-icon {
    width: 32px;
    height: 32px;
    margin-left: 14px;
  }
</style>
</head>
<body>
  <main class="card">
    <svg class="bands" viewBox="0 0 1200 720" aria-hidden="true">
      <polygon class="band-yellow" points="0,538 680,538 480,720 0,720"/>
      <polygon class="band-blue" points="711,538 1200,538 1200,720 500,720"/>
    </svg>

    <header class="holder">
      <p class="holder-name">Dale Pickett</p>
      <p class="holder-role">Manager</p>
    </header>

    <div class="truck-art" role="img" aria-label="Illustration of a green garbage truck with a yellow bin"></div>

    <h1 class="brand-name">
      <span class="word-line">Harbor Refuse</span>
      <span class="number-line">342</span>
    </h1>

    <p class="contact-email">
      <svg class="contact-icon" viewBox="0 0 24 24" aria-hidden="true">
        <rect x="2" y="5" width="20" height="14" fill="#161616"/>
        <polyline points="2,5 12,13 22,5" fill="none" stroke="#f8d00f" stroke-width="1.8"/>
      </svg>
      harborrefuse342@quillmail.com.au
    </p>

    <p class="phone">
      0439516204
      <svg class="phone-icon" viewBox="0 0 24 24" aria-hidden="true">
        <path fill="#ffffff" d="M6.6 10.8c1.4 2.8 3.8 5.1 6.6 6.6l2.2-2.2c.3-.3.7-.4 1-.2 1.1.4 2.3.6 3.6.6.6 0 1 .4 1 1V20c0 .6-.4 1-1 1C10.6 21 3 13.4 3 4c0-.6.4-1 1-1h3.5c.6 0 1 .4 1 1 0 1.3.2 2.5.6 3.6.1.3 0 .7-.2 1l-2.3 2.2z"/>
      </svg>
    </p>
  </main>
</body>
</html>
```